Wordpress site for cyber security and network perfomance software vendor

We need a brand new Wordpress website consisting of a single home/landing page and page template so that we can add pages in future.
The website is intended to provide information to prospects and customers. The homepage should have a top menu bar that is customizable similar to what we already have at qelvora.com.
Note that we are after a new design – that is, please don’t reference our existing website for design inspiration (qelvora.com)
We are after a Wordpress site that may be implemented straight onto our Wordpress hoster (HostMarrow) .
Quillmo is a software company delivering a solution for customers to get visibility of network performance and cyber security. The Quillmo solution reduces cyber security risk, identifies performance bottlenecks and ultimately lower costs by reducing the number of tools need to monitor the IT environment
We deliver network performance and cyber security information to the IT manager and network teams in a format that they understand, at a realistic cost, and requiring minimal resource to implement. This is a crowded market, most competitors provide highly complex, expensive and highly customized tools to large enterprise. Quillmo makes this style of visibility tool accessible to the mid market.

Target Market(s)

IT Managers, network engineers, mid market organisations, IT service providers

Industry/Entity Type

IT

Font styles to use
Sans Serif

Colors
0094D4
00A9DD
6FCCEA
C7EBF8
E9F6FB

Requirements
Must have
• Fully coded for WordPress. Responsive and mobile friendly. The website copy is provided in the attached document. Utilise the Quillmo logo colors as part of the design (Dark Blue: 2E4F99, Light Blue: 00AFF4, Green: 73D94F). Top Horizontal menu bar for additional pages. Implement one of our screenshots (I have included a bunch of screenshots to choose from)
Nice to have
• Icons, panels or infographics matching the services. Our existing site is built using Pelk – this is not a requirement for the new site but a nice to have as we are familiar with Pelk.
Should not have
• Preferably no corporate images – business people shaking hands or teams of people a meeting room (or that kind of thing)

```html
<!DOCTYPE html>
<html lang="en">
<head>
<meta charset="utf-8">
<title>Quillmo — Security + Visibility</title>
<link rel="stylesheet" href="https://fonts.googleapis.com/css2?family=Poppins:ital,wght@0,400;0,500;0,600;0,700;1,400&family=Roboto+Slab:wght@400&display=swap">
<style>
:root{
  --navy:#0d3b7c;
  --navy-deep:#062a5c;
  --blue:#1d8ee6;
  --sky:#00a9dd;
  --green:#8bd14f;
  --green-soft:#b5e27a;
  --ice:#e9f6fb;
  --ice-2:#c7ebf8;
  --ink:#111a26;
  --grey:#6b7380;
  --field:#eef0f3;
  --white:#ffffff;
  --footer:#07101c;
}
*{box-sizing:border-box;margin:0;padding:0}
html,body{width:1200px;height:4854px;overflow:hidden}
body{position:relative;font-family:'Poppins',sans-serif;color:var(--ink);background:var(--white)}
.abs{position:absolute}
.section{position:absolute;left:0;width:1200px}
svg{display:block}

/* header */
.hero{top:0;height:650px}
.hero-bg{position:absolute;inset:0}
.nav{position:absolute;top:0;left:0;width:1200px;height:60px}
.brand{position:absolute;display:flex;align-items:center;gap:8px;color:var(--white);font-weight:500;font-size:26px}
.brand-dot{width:30px;height:30px;border-radius:50%;background:var(--white)}
.nav-links{position:absolute;left:466px;top:20px;display:flex;gap:24px;font-size:12px;color:var(--white)}
.btn-demo{position:absolute;left:812px;top:12px;width:120px;height:36px;background:var(--white);color:var(--navy);font-size:12px;font-weight:600;display:flex;align-items:center;justify-content:center;border-radius:2px}
.hero-title{position:absolute;left:62px;top:238px;font-size:48px;font-weight:500;color:var(--white);letter-spacing:-.5px}
.hero-sub{position:absolute;left:62px;top:312px;font-family:'Roboto Slab',serif;font-size:14px;color:var(--white)}
.btn-light{position:absolute;left:62px;top:367px;width:115px;height:34px;background:var(--white);color:var(--navy);font-size:12px;font-weight:500;display:flex;align-items:center;justify-content:center;border-radius:3px}
.screen{position:absolute;left:625px;top:228px;width:570px;height:340px}

/* specialising */
.intro h2{position:absolute;left:530px;top:770px;width:560px;font-size:24px;font-weight:600;line-height:34px}
.accent{color:var(--blue)}
.ring-list{position:absolute;left:530px;top:900px;width:520px;list-style:none}
.ring-list li{position:relative;padding-left:38px;font-size:11.5px;line-height:19.5px;color:var(--grey);margin-bottom:14px}
.ring-list li::before{content:"";position:absolute;left:0;top:4px;width:12px;height:12px;border-radius:50%;border:3px solid var(--navy)}

/* why */
.why h2{position:absolute;left:635px;top:1258px;font-size:26px;font-weight:600}
.why .copy{position:absolute;left:635px;top:1308px;width:415px;font-size:11.5px;line-height:19.5px;color:#333}
.why .copy p{margin-bottom:10px}

/* deliver */
.center-title{position:absolute;left:0;width:1200px;text-align:center;font-size:26px;font-weight:600}
.feature-card{position:absolute;left:150px;top:1990px;width:270px;color:var(--white)}
.feature-card h3{font-size:17px;font-weight:600;line-height:26px;color:var(--ink);margin-bottom:40px}
.feature-card p{font-size:11.5px;line-height:19.5px}
.tabs{position:absolute;left:855px;top:1938px;width:285px}
.tab{height:38px;margin-bottom:22px;border-radius:20px 0 0 20px;background:#eef1f4;display:flex;align-items:center;font-size:12px;color:#333;position:relative}
.tab span{position:absolute;left:0;right:0;text-align:center;padding-left:40px}
.tab svg{position:absolute;left:30px;top:13px}
.tab.active{background:var(--navy);color:var(--white)}

/* committed */
.committed .heading{position:absolute;left:0;top:2492px;width:1200px;text-align:center;color:var(--white);font-size:26px;font-weight:500;line-height:38px}
.bubble{position:absolute;width:210px;height:210px;border-radius:50%;background:var(--white);display:flex;flex-direction:column;align-items:center;justify-content:center;gap:20px;font-size:20px;font-weight:600;color:var(--navy)}
.bubble.dark{background:var(--navy);color:var(--white)}
.bubble-icon{width:58px;height:58px;border-radius:8px;background:var(--ice);display:flex;align-items:center;justify-content:center}
.bubble.dark .bubble-icon{background:#24508f}

/* testimonial */
.quote .label{position:absolute;left:552px;top:3093px;font-size:11px;color:#333}
.quote h2{position:absolute;left:552px;top:3115px;font-size:28px;font-weight:600}
.quote .body{position:absolute;left:552px;top:3168px;width:430px;font-size:11.5px;line-height:20px;font-style:italic;color:var(--grey)}
.quote .name{position:absolute;left:552px;top:3272px;font-size:12px;font-weight:600;color:var(--navy);letter-spacing:.5px}

/* no obligations */
.obl h2{position:absolute;left:62px;top:3556px;font-size:28px;font-weight:600}
.obl .copy{position:absolute;left:62px;top:3615px;width:445px;font-size:11.5px;line-height:19.5px;color:#333}
.btn-navy{position:absolute;width:115px;height:36px;background:var(--navy);color:var(--white);font-size:12px;font-weight:500;display:flex;align-items:center;justify-content:center;border-radius:3px}

/* call form */
.form-card{position:absolute;left:640px;top:4030px;width:410px;height:440px;background:var(--white);border-radius:40px;box-shadow:0 10px 40px rgba(13,59,124,.08)}
.form-card h2{position:absolute;left:40px;top:35px;font-size:28px;font-weight:600}
.form-phone{position:absolute;left:40px;top:88px;display:flex;align-items:center;gap:12px;font-size:12px;font-weight:500}
.icon-ring{width:34px;height:34px;border-radius:50%;border:2px solid var(--green);display:flex;align-items:center;justify-content:center}
.field{position:absolute;left:40px;width:300px;height:34px;background:var(--field);border-radius:3px;font-size:11px;color:var(--grey);padding:0 16px;display:flex;align-items:center}

/* footer */
.footer{top:4500px;height:354px}
.footer h4{position:absolute;font-size:16px;font-weight:500;color:var(--blue)}
.foot-links{position:absolute;left:432px;top:4556px;list-style:none}
.foot-links li{font-size:12px;color:var(--white);height:30px;display:flex;align-items:center;gap:14px}
.foot-links li::before{content:"";width:9px;height:9px;border-radius:50%;border:2px solid var(--green)}
.social{position:absolute;top:4690px;width:28px;height:28px;border-radius:50%;background:var(--white)}
.contact-row{position:absolute;left:796px;display:flex;align-items:center;gap:18px}
.contact-row .city{font-size:11px;color:var(--green)}
.contact-row .num{font-size:12px;font-weight:600;color:var(--white);margin-top:4px}
.copyright{position:absolute;left:0;top:4830px;width:1200px;height:24px;background:linear-gradient(90deg,var(--green),var(--blue));color:var(--white);font-size:11px;display:flex;align-items:center;justify-content:center}
</style>
</head>
<body>

<!-- HERO -->
<header class="section hero">
  <svg class="hero-bg" width="1200" height="650" viewBox="0 0 1200 650">
    <defs>
      <linearGradient id="heroPhoto" x1="0" y1="0" x2="1" y2="1">
        <stop offset="0" stop-color="#4f9a62"/>
        <stop offset=".55" stop-color="#3e8d7f"/>
        <stop offset="1" stop-color="#1d6fb8"/>
      </linearGradient>
      <linearGradient id="heroBlue" x1="0" y1="0" x2="1" y2="1">
        <stop offset="0" stop-color="#1f93ee"/>
        <stop offset="1" stop-color="#0a62cf"/>
      </linearGradient>
    </defs>
    <path role="img" aria-label="Server room with network monitoring screens, green tint" d="M0 0H1200V520C1000 630 760 660 580 648C330 632 120 600 0 560Z" fill="url(#heroPhoto)"/>
    <path d="M600 0H1200V560C1080 640 860 660 700 640C600 560 560 420 580 260C590 140 600 60 600 0Z" fill="url(#heroBlue)"/>
    <rect x="895" y="130" width="8" height="58" rx="4" transform="rotate(40 899 159)" fill="#9fe0a8" opacity=".8"/>
    <circle cx="732" cy="618" r="40" fill="#6fccea" opacity=".35"/>
  </svg>

  <nav class="nav">
    <div class="brand" style="left:62px;top:14px"><span class="brand-dot"></span>Quillmo</div>
    <div class="nav-links"><span>Home</span><span>Product</span><span>Blog</span><span>About</span><span>Partner Portal</span></div>
    <div class="btn-demo">DEMO LOGIN</div>
  </nav>

  <h1 class="hero-title">SECURITY + VISIBILITY</h1>
  <p class="hero-sub">Network Monitoring for IT Perfomance and Security</p>
  <div class="btn-light">CONTACT US</div>

  <svg class="screen" width="570" height="340" viewBox="0 0 570 340">
    <rect x="0" y="0" width="565" height="330" rx="12" fill="#1a1d22"/>
    <rect role="img" aria-label="Quillmo performance dashboard screenshot" x="14" y="14" width="537" height="300" fill="#23272e"/>
    <rect x="14" y="14" width="537" height="14" fill="#2e3440"/>
    <polyline points="40,160 70,150 95,158 120,140 145,155 170,148 200,162 230,138 260,152 290,146 320,158 350,140 380,150 410,144 440,156 470,138 500,150 530,146" fill="none" stroke="#3da7ff" stroke-width="1.5"/>
    <g fill="#3a8fd6">
      <rect x="40" y="210" width="40" height="5"/><rect x="40" y="220" width="55" height="5"/><rect x="40" y="230" width="30" height="5"/><rect x="40" y="240" width="48" height="5"/>
      <rect x="175" y="210" width="50" height="5"/><rect x="175" y="220" width="35" height="5"/><rect x="175" y="230" width="60" height="5"/><rect x="175" y="240" width="25" height="5"/>
      <rect x="305" y="210" width="38" height="5"/><rect x="305" y="220" width="52" height="5"/><rect x="305" y="230" width="44" height="5"/>
      <rect x="435" y="210" width="58" height="5"/><rect x="435" y="220" width="32" height="5"/><rect x="435" y="230" width="46" height="5"/>
    </g>
    <rect x="-25" y="330" width="600" height="8" rx="4" fill="#8d939a"/>
  </svg>
</header>

<!-- SPECIALISING -->
<section class="section intro" style="top:650px;height:480px">
  <svg class="abs" style="left:60px;top:70px" width="380" height="380" viewBox="0 0 380 380">
    <circle role="img" aria-label="Quillmo brand emblem" cx="190" cy="190" r="175" fill="#e9f6fb"/>
  </svg>
  <h2 style="top:120px">Specialising in IT <span class="accent">Network Performance</span> and Cyber Security Solutions for Small to Medium Organisations.</h2>
  <ul class="ring-list" style="top:250px">
    <li>Do you feel concerned about your network performance, and cyber threats, but you don't have the time or staff to deal with it?</li>
    <li>Perhaps you've outsourced your IT support and have discovered that your service provider doesn't have visibility of you network?</li>
    <li>It's not easy being an IT manager. Especially if you work in a small to medium sized organisation. You're typically stretched to the limit with an understaffed team and there's simply not enough hours in the day to tackle all the increasing demands.</li>
  </ul>
</section>

<!-- WHY -->
<section class="section why" style="top:1125px;height:600px">
  <svg class="abs" style="left:0;top:0" width="1200" height="600" viewBox="0 0 1200 600">
    <defs>
      <linearGradient id="whyBg" x1="0" y1="0" x2="1" y2="0">
        <stop offset="0" stop-color="#eef8fc"/><stop offset="1" stop-color="#c7ebf8"/>
      </linearGradient>
      <clipPath id="whyClip"><circle cx="250" cy="330" r="300"/></clipPath>
    </defs>
    <path d="M0 0C250 60 700 70 1200 10V600H0Z" fill="url(#whyBg)"/>
    <circle cx="250" cy="330" r="300" fill="#0b3a7e"/>
    <rect role="img" aria-label="Smiling IT manager working on a laptop" x="0" y="120" width="520" height="480" clip-path="url(#whyClip)" fill="#1e4f8f" opacity=".6"/>
  </svg>
  <h2 style="top:133px">Why Quillmo ?</h2>
  <div class="copy" style="top:183px">
    <p>At Quillmo, we understand the challenges that you face. Cyber security and network incidents can have devastating impacts on small to medium organisations because you typically don't have the time, staff, or resources to develop complicated responses to cyber security threats.</p>
    <p>That's why small to medium sized organisations are vulnerable to potentially devastating cyber incidents. Did you know that on average, it took over 220 days for organisations to identify a breach and a further 80 days to contain the breach? (Norvane Research, 2020).</p>
    <p>With Quillmo, you can avoid these unpleasant surprises.</p>
    <p>We're committed to providing the best easy-to-use cyber tools for small to medium organisations that will give you visibility across your network, performance, AND cyber security data. So, you won't get any nasty surprises.</p>
  </div>
</section>

<!-- DELIVER -->
<section class="section deliver" style="top:1725px;height:620px">
  <h2 class="center-title" style="top:62px">We deliver <span class="accent">everything</span> you need</h2>
  <svg class="abs" style="left:0;top:0" width="850" height="620" viewBox="0 0 850 620">
    <defs>
      <linearGradient id="featGrad" x1="0" y1="0" x2="1" y2="1">
        <stop offset="0" stop-color="#a6e05a"/><stop offset="1" stop-color="#1f8fd8"/>
      </linearGradient>
      <linearGradient id="photoGrad" x1="0" y1="0" x2="1" y2="1">
        <stop offset="0" stop-color="#1a6fc9"/><stop offset="1" stop-color="#06204a"/>
      </linearGradient>
    </defs>
    <circle cx="270" cy="350" r="210" fill="url(#featGrad)"/>
    <circle role="img" aria-label="Hands holding a tablet with glowing analytics charts" cx="550" cy="350" r="210" fill="url(#photoGrad)" opacity=".92"/>
    <circle cx="700" cy="440" r="78" fill="#0b3a7e" opacity=".85"/>
    <circle cx="395" cy="513" r="9" fill="#1d6fd0"/>
  </svg>
  <div class="feature-card" style="top:265px">
    <h3>Sophisticated Data<br>Analytics</h3>
    <p>Powerful data analytics correlate threat data and anomalous traffic data with network performance to deliver meaningful information so you can easily respond.</p>
  </div>
  <div class="tabs" style="top:213px">
    <div class="tab active"><svg width="8" height="12" viewBox="0 0 8 12"><path d="M7 1L2 6l5 5" fill="none" stroke="currentColor" stroke-width="1.6"/></svg><span>Sophisticated Data Analytics</span></div>
    <div class="tab"><svg width="8" height="12" viewBox="0 0 8 12"><path d="M7 1L2 6l5 5" fill="none" stroke="#333" stroke-width="1.6"/></svg><span>Best Visual Analytics</span></div>
    <div class="tab"><svg width="8" height="12" viewBox="0 0 8 12"><path d="M7 1L2 6l5 5" fill="none" stroke="#333" stroke-width="1.6"/></svg><span>Best Visual Analytics</span></div>
    <div class="tab"><svg width="8" height="12" viewBox="0 0 8 12"><path d="M7 1L2 6l5 5" fill="none" stroke="#333" stroke-width="1.6"/></svg><span>Best Visual Analytics</span></div>
    <div class="tab"><svg width="8" height="12" viewBox="0 0 8 12"><path d="M7 1L2 6l5 5" fill="none" stroke="#333" stroke-width="1.6"/></svg><span>Best Visual Analytics</span></div>
  </div>
</section>

<!-- COMMITTED -->
<section class="section committed" style="top:2345px;height:600px">
  <svg class="abs" style="left:0;top:0" width="1200" height="600" viewBox="0 0 1200 600">
    <defs>
      <linearGradient id="bandGrad" x1="0" y1="0" x2="1" y2="0">
        <stop offset="0" stop-color="#7cc95a"/><stop offset=".5" stop-color="#2c9bd0"/><stop offset="1" stop-color="#0b7fe6"/>
      </linearGradient>
    </defs>
    <path role="img" aria-label="Blurred data centre backdrop with green to blue overlay" d="M0 60C400 20 800 0 1200 0V520C800 610 400 610 0 530Z" fill="url(#bandGrad)"/>
    <path d="M160 290L175 360L240 340Z" fill="#fff"/>
    <path d="M820 290L835 360L900 340Z" fill="#fff"/>
    <path d="M500 480L540 430L560 470Z" fill="#0d3b7c"/>
  </svg>
  <h2 class="heading" style="top:147px">we're committed to providing you the best<br>easy-to-use tools</h2>
  <div class="bubble" style="left:155px;top:310px">
    <div class="bubble-icon"><svg width="30" height="30" viewBox="0 0 30 30"><path d="M3 15C7 8 23 8 27 15C23 22 7 22 3 15Z" fill="none" stroke="#1d8ee6" stroke-width="2"/><circle cx="15" cy="15" r="4" fill="#1d8ee6"/></svg></div>
    Visibility
  </div>
  <div class="bubble dark" style="left:495px;top:290px">
    <div class="bubble-icon"><svg width="30" height="30" viewBox="0 0 30 30"><circle cx="13" cy="13" r="9" fill="none" stroke="#fff" stroke-width="2"/><rect x="17" y="18" width="9" height="8" rx="1" fill="#fff"/></svg></div>
    security
  </div>
  <div class="bubble" style="left:815px;top:310px">
    <div class="bubble-icon"><svg width="30" height="30" viewBox="0 0 30 30"><path d="M8 24V18C4 16 4 8 10 6C15 3 24 6 24 13L26 17H23V22H18V26" fill="none" stroke="#1d8ee6" stroke-width="2"/></svg></div>
    peace of mind
  </div>
</section>

<!-- TESTIMONIAL -->
<section class="section quote" style="top:2945px;height:490px">
  <svg class="abs" style="left:210px;top:70px" width="240" height="420" viewBox="0 0 240 420">
    <circle role="img" aria-label="Client portrait" cx="152" cy="72" r="55" fill="#c9d3dc"/>
    <circle role="img" aria-label="Client portrait" cx="83" cy="201" r="75" fill="#d9cfc8"/>
    <circle role="img" aria-label="Client portrait" cx="152" cy="345" r="50" fill="#b8c1c9"/>
    <circle cx="185" cy="222" r="17" fill="#7ad14f"/>
    <circle cx="208" cy="259" r="7" fill="#7ad14f"/>
  </svg>
  <p class="label" style="top:148px">What Our Client Say</p>
  <h2 style="top:170px">We would <span class="accent">love to hear</span> from you.</h2>
  <p class="body" style="top:225px">Lorem Ipsum is simply dummy text of the printing and typesetting industry. Lorem Ipsum has been the industry's standard dummy text ever since the 1500s, when an unknown printer took a galley of type and scrambled it to make a type specimen book.</p>
  <p class="name" style="top:327px">DARA KELLEN</p>
  <svg class="abs" style="left:552px;top:360px" width="100" height="4"><rect width="36" height="2" fill="#1d8ee6"/><rect x="44" width="22" height="2" fill="#c7ebf8"/><rect x="74" width="22" height="2" fill="#c7ebf8"/></svg>
</section>

<!-- NO OBLIGATIONS -->
<section class="section obl" style="top:3435px;height:580px">
  <svg class="abs" style="left:0;top:0" width="1200" height="580" viewBox="0 0 1200 580">
    <defs>
      <linearGradient id="oblGrad" x1="0" y1="0" x2="1" y2="0">
        <stop offset="0" stop-color="#e4f3df"/><stop offset=".5" stop-color="#e9f6fb"/><stop offset="1" stop-color="#bfe3f6"/>
      </linearGradient>
    </defs>
    <path d="M0 0C400 40 800 40 1200 10V500C800 560 400 560 0 500Z" fill="url(#oblGrad)"/>
    <rect x="630" y="133" width="540" height="295" rx="6" fill="#1b1e24"/>
    <rect role="img" aria-label="Quillmo dashboard screenshot with traffic line chart and donut charts" x="638" y="141" width="524" height="279" fill="#262a31"/>
    <polyline points="660,250 700,240 740,252 780,230 820,246 860,238 900,250 940,228 980,244 1020,236 1060,248 1100,232 1140,242" fill="none" stroke="#3da7ff" stroke-width="1.5"/>
    <circle cx="680" cy="345" r="22" fill="none" stroke="#3da7ff" stroke-width="7"/>
    <circle cx="865" cy="345" r="22" fill="none" stroke="#2f6fb0" stroke-width="7"/>
    <circle cx="1050" cy="345" r="22" fill="none" stroke="#3da7ff" stroke-width="7"/>
  </svg>
  <h2 style="top:121px">No obligations</h2>
  <div class="copy" style="top:180px">At Quillmo, we have designed a network performance monitoring and cyber security visibility solution that is both simple and comprehensive, that is, simple to install yet comprehensive in the functionality and benefit to your business. In the simplest form there are 2 components, an appliance which isn installed on site and collects statistical information and continuously listens out for malicious activity, and a web based reporting dashboard living in the cloud that presents the information in a clear and concise format.</div>
  <div class="btn-navy" style="left:62px;top:360px">CONTACT US</div>
</section>

<!-- CALL -->
<section class="section call" style="top:4015px;height:485px">
  <svg class="abs" style="left:60px;top:15px" width="480" height="470" viewBox="0 0 480 470">
    <defs>
      <linearGradient id="callGrad" x1="0" y1="0" x2="1" y2="1">
        <stop offset="0" stop-color="#cfe9f7"/><stop offset="1" stop-color="#1d8ee6"/>
      </linearGradient>
    </defs>
    <path role="img" aria-label="Man in glasses holding a laptop" d="M60 120C120 30 330 20 400 110C470 200 450 380 330 440C210 490 60 420 30 300C15 230 30 170 60 120Z" fill="url(#callGrad)" opacity=".7"/>
  </svg>
  <div class="form-card" style="top:15px">
    <h2>Give us <span class="accent">a call!</span></h2>
    <div class="form-phone"><span class="icon-ring"><svg width="14" height="14" viewBox="0 0 14 14"><path d="M3 1L5 4L4 6C5 8 6 9 8 10L10 9L13 11L12 13C7 13 1 7 1 2Z" fill="#8bd14f"/></svg></span>+123 456 7890</div>
    <div class="field" style="top:138px">First Name :</div>
    <div class="field" style="top:183px">Last Name :</div>
    <div class="field" style="top:228px">Email :</div>
    <div class="field" style="top:273px">Company :</div>
    <div class="btn-navy" style="left:40px;top:323px">CONTACT US</div>
  </div>
</section>

<!-- FOOTER -->
<footer class="section footer">
  <svg class="abs" style="left:0;top:0" width="1200" height="330" viewBox="0 0 1200 330">
    <defs>
      <linearGradient id="footGrad" x1="0" y1="0" x2="1" y2="1">
        <stop offset="0" stop-color="#0c1a2c"/><stop offset="1" stop-color="#040a12"/>
      </linearGradient>
    </defs>
    <path role="img" aria-label="Dark office backdrop with whiteboard" d="M0 20C400 0 800 0 1200 20V330H0Z" fill="url(#footGrad)"/>
  </svg>
  <div class="brand" style="left:62px;top:92px;font-size:30px;color:#1d8ee6"><span class="brand-dot" style="background:#8bd14f"></span>Quillmo</div>
</footer>
<span class="social" style="left:62px"></span>
<span class="social" style="left:98px"></span>
<span class="social" style="left:134px"></span>

<h4 class="abs" style="left:432px;top:4520px;font-size:16px;font-weight:500;color:var(--blue)">Site Map</h4>
<ul class="foot-links">
  <li>Home</li><li>About Us</li><li>Product</li><li>Blog</li><li>About Us</li><li>Partner Portal</li><li>Demo Login</li>
</ul>

<h4 class="abs" style="left:804px;top:4520px;font-size:16px;font-weight:500;color:var(--blue)">Give us a call!</h4>
<div class="contact-row" style="top:4562px">
  <span class="icon-ring"><svg width="14" height="14" viewBox="0 0 14 14"><path d="M3 1L5 4L4 6C5 8 6 9 8 10L10 9L13 11L12 13C7 13 1 7 1 2Z" fill="#8bd14f"/></svg></span>
  <div><div class="city">Australia</div><div class="num">+61 2 5550 1834</div></div>
</div>
<div class="contact-row" style="top:4630px">
  <span class="icon-ring"><svg width="14" height="14" viewBox="0 0 14 14"><path d="M3 1L5 4L4 6C5 8 6 9 8 10L10 9L13 11L12 13C7 13 1 7 1 2Z" fill="#8bd14f"/></svg></span>
  <div><div class="city">Germany</div><div class="num">+49 69 555 01 892</div></div>
</div>

<div class="copyright">Copyright Quillmo 2020 - All Right Reserved.</div>

</body>
</html>
```